New Corporate Business Card - Velmorabelle

What we need:
We need a new corporate business card.
We want a new template that we can change by ourself.
We want business card modern and minimalist but that looks professional.
We will print it in 300 gr soft-touch.
Why not a white side with the logo and a red/grey side with the content?
Why not a grey side and a red side like our logo?
I am sure that you have better idea than ours that's the reason we come here.

Who we are:
We are a private label company in cosmetics based in Switzerland. We work in BtoB. We make skin care products for other brands.

Target Market(s)

B to B - Worldwide - any gender

Industry/Entity Type

Cosmetics

Contact Information for Business Card

Side 1:
Logo
Your Swiss Private Label Manufacturer or www.velmorabelle.ch

Side 2:
Name and surname (Example: Lucien Marchetaz)
Job Description (General Manager)
Telephone (+41 32 918 64 00)
Direct (+41 32 918 64 64)
Email (lucien.marchetaz@velmorabelle.ch)
Chemin des Prés-Fleuris 14, 2000 Neuchâtel, Switzerland
www.velmorabelle.ch

Font styles to use
Serif
Sans Serif

Requirements
Must have
• You can use 4 colors: white, red, grey and/or black .
Should not have
• Too much colors, too much things. We want it simple!

```html
<!DOCTYPE html>
<html lang="en">
<head>
<meta charset="utf-8">
<title>Velmorabelle – Business Card</title>
<link rel="stylesheet" href="https://fonts.googleapis.com/css2?family=Open+Sans:wght@300;400;600&display=swap">
<style>
  :root {
    --brand-red: #d22e26;
    --brand-grey: #a7a8aa;
    --paper-white: #ffffff;
    --backdrop: #e8e6e3;
    --card-shadow: rgba(0, 0, 0, 0.18);
  }
  * { box-sizing: border-box; margin: 0; padding: 0; }
  html, body {
    width: 1200px;
    height: 873px;
    overflow: hidden;
    background: var(--backdrop);
    font-family: "Open Sans", Arial, sans-serif;
  }
  .card-sheet {
    width: 1200px;
    height: 873px;
    display: flex;
    align-items: center;
    justify-content: center;
    gap: 60px;
  }
  .card {
    position: relative;
    width: 500px;
    height: 324px;
    box-shadow: 0 8px 24px var(--card-shadow);
    color: var(--paper-white);
  }
  .card--contact { background: var(--brand-red); }
  .card--brand { background: var(--brand-grey); }

  /* Contact side */
  .person { position: absolute; left: 36px; top: 34px; }
  .person__name {
    font-size: 19px;
    font-weight: 400;
    text-transform: uppercase;
    letter-spacing: 0.2px;
  }
  .person__role {
    font-size: 10px;
    font-weight: 400;
    letter-spacing: 3px;
    margin-top: 2px;
  }
  .person__rule {
    width: 28px;
    height: 1.5px;
    background: var(--paper-white);
    margin: 10px 0 8px;
  }
  .contact-list { list-style: none; font-size: 10.5px; line-height: 17px; }
  .contact-list li { display: flex; align-items: center; gap: 7px; }
  .contact-list .icon { width: 10px; height: 10px; flex: none; }
  .contact-list .no-icon { width: 10px; flex: none; }

  .wordmark {
    position: absolute;
    display: flex;
    align-items: center;
    gap: 10px;
    font-weight: 300;
    color: var(--paper-white);
  }
  .wordmark__square { flex: none; background: var(--paper-white); }
  .card--contact .wordmark { right: 36px; top: 128px; font-size: 24px; letter-spacing: 2px; }
  .card--contact .wordmark__square { width: 14px; height: 14px; background: var(--brand-grey); }

  .address {
    position: absolute;
    right: 36px;
    bottom: 28px;
    text-align: right;
    font-size: 12px;
    line-height: 17px;
  }

  /* Brand side */
  .card--brand .wordmark {
    left: 0; right: 0; top: 126px;
    justify-content: center;
    font-size: 34px;
    letter-spacing: 3px;
  }
  .card--brand .wordmark__square { width: 18px; height: 18px; background: var(--brand-red); }
  .tagline {
    position: absolute;
    left: 0; right: 0;
    top: 196px;
    text-align: center;
    font-size: 11.5px;
    letter-spacing: 0.3px;
  }
</style>
</head>
<body>
<main class="card-sheet">
  <section class="card card--contact" aria-label="Contact side">
    <div class="person">
      <h1 class="person__name">Lucien Marchetaz</h1>
      <p class="person__role">General Manager</p>
      <div class="person__rule"></div>
      <ul class="contact-list">
        <li>
          <svg class="icon" viewBox="0 0 10 10" aria-hidden="true"><path d="M2 0.8 L3.6 2.8 L2.8 3.8 Q4 6 6.2 7.2 L7.2 6.4 L9.2 8 L8 9.4 Q3.5 9 0.6 2 Z" fill="#fff"/></svg>
          <span>Tel. +41 32 918 64 00</span>
        </li>
        <li><span class="no-icon"></span><span>Direct. +41 32 918 64 64</span></li>
        <li>
          <svg class="icon" viewBox="0 0 10 10" aria-hidden="true"><rect x="0.7" y="2" width="8.6" height="6" fill="none" stroke="#fff" stroke-width="1"/><path d="M0.7 2 L5 5.6 L9.3 2" fill="none" stroke="#fff" stroke-width="1"/></svg>
          <span>lucien.marchetaz@velmorabelle.ch</span>
        </li>
        <li>
          <svg class="icon" viewBox="0 0 10 10" aria-hidden="true"><circle cx="5" cy="5" r="4.3" fill="none" stroke="#fff" stroke-width="1"/><ellipse cx="5" cy="5" rx="1.8" ry="4.3" fill="none" stroke="#fff" stroke-width="0.8"/><path d="M0.7 5 H9.3" stroke="#fff" stroke-width="0.8"/></svg>
          <span>www.velmorabelle.ch</span>
        </li>
      </ul>
    </div>

    <div class="wordmark"><span class="wordmark__square"></span><span>Velmorabelle</span></div>

    <address class="address" style="font-style: normal;">
      Chemin des Prés-Fleuris 14,<br>
      2000 Neuchâtel, Switzerland
    </address>
  </section>

  <section class="card card--brand" aria-label="Brand side">
    <div class="wordmark"><span class="wordmark__square"></span><span>Velmorabelle</span></div>
    <p class="tagline">Your Swiss Private Label Manufacturer</p>
  </section>
</main>
</body>
</html>
```